New Album "A night beside the silver hills"

I need a cd cover for a new pop rock album called "A night beside the silver hills"
The main color of the artwork shall obviously be orange. The artwork shouldn't be too "obvious", but it would be better something a bit abstract.
Please remember that it is a Music Cd Cover, so do not send business logo or advertisement images.

Target Market(s)

It's a pop rock album, so the target customers are young and adult people from 15-60 years old

Requirements
Must have
• Orange as main colour
The Artist name is: Remy Castellan
The Title: A night beside the silver hills
Should not have
• Not too cheesy or dreamy images please. No simple sunset or sunrise pics

```html
<!DOCTYPE html>
<html lang="en">
<head>
<meta charset="UTF-8">
<title>A night beside the silver hills — Remy Castellan</title>
<link rel="stylesheet" href="https://fonts.googleapis.com/css2?family=Questrial&display=swap">
<style>
  :root {
    --ink-black: #0b0604;
    --smoke-yellow: #f6d64a;
    --smoke-amber: #f3a21c;
    --smoke-orange: #ee6a12;
    --smoke-rust: #9a3a0c;
    --smoke-cream: #fbeede;
    --smoke-mist: #dfe6ea;
    --smoke-rose: #f6c9bd;
    --title-white: #ffffff;
    --artist-dark: #1a0d06;
  }
  html, body {
    margin: 0;
    padding: 0;
    width: 1200px;
    height: 1200px;
    overflow: hidden;
    background: var(--ink-black);
  }
  .cover {
    position: relative;
    width: 1200px;
    height: 1200px;
    overflow: hidden;
    font-family: "Questrial", "Helvetica Neue", Arial, sans-serif;
  }
  .cover-artwork {
    position: absolute;
    inset: 0;
    background:
      radial-gradient(ellipse 22% 18% at 86% 46%, rgba(255,255,250,0.85), transparent 70%),
      radial-gradient(ellipse 28% 22% at 80% 34%, rgba(253,240,225,0.9), transparent 72%),
      radial-gradient(ellipse 40% 25% at 55% 92%, rgba(250,245,242,0.95), transparent 70%),
      radial-gradient(ellipse 35% 20% at 90% 95%, var(--smoke-mist), transparent 75%),
      radial-gradient(ellipse 20% 20% at 10% 88%, var(--smoke-rose), transparent 75%),
      radial-gradient(ellipse 25% 30% at 96% 12%, var(--smoke-rust), transparent 75%),
      radial-gradient(ellipse 22% 20% at 30% 8%, var(--smoke-yellow), transparent 70%),
      radial-gradient(ellipse 18% 22% at 3% 40%, var(--smoke-yellow), transparent 70%),
      radial-gradient(ellipse 35% 35% at 30% 40%, var(--smoke-orange), transparent 75%),
      radial-gradient(ellipse 30% 25% at 55% 60%, var(--smoke-amber), transparent 75%),
      radial-gradient(ellipse 14% 10% at 4% 2%, var(--ink-black), transparent 80%),
      linear-gradient(160deg, var(--smoke-amber) 0%, var(--smoke-orange) 40%, #e58a4a 70%, var(--smoke-cream) 100%);
  }
  .cover-title,
  .cover-artist {
    position: absolute;
    left: 39px;
    margin: 0;
    font-weight: 400;
    text-transform: uppercase;
    white-space: nowrap;
    line-height: 1;
  }
  .cover-title {
    top: 585px;
    font-size: 47px;
    letter-spacing: 0.07em;
    color: var(--title-white);
  }
  .cover-artist {
    top: 680px;
    font-size: 47px;
    letter-spacing: 0.07em;
    color: var(--artist-dark);
  }
</style>
</head>
<body>
  <main class="cover">
    <div class="cover-artwork" role="img" aria-label="Abstract photograph of swirling orange, amber and yellow ink smoke with pale white clouds and a dark rust corner"></div>
    <h1 class="cover-title">A night beside the silver hills</h1>
    <p class="cover-artist">Remy Castellan</p>
  </main>
</body>
</html>
```